Consulting and investment firm, logo design is needed as well.

I am looking to open a consulting firm. Where myself is currently an investor, entrepreneur and consultant for many businesses.

The company name is Morvik Company Limited
The logo should communicate prestige like luxury or gold or money, trustworthy and modern.

Overall name card Color can be: white, black, blue, gold, silver (you can choose one, few or all of it, up to you)

It would be great if you can provide raw file like .psd for me so that I can make some little amendment in future and inserting company name or remove it. Because I would also like to use it as only under my name too (some card I will remove the company name).

• I want it to look modern.

```html
<!DOCTYPE html>
<html lang="en">
<head>
<meta charset="utf-8">
<title>Morvik Company Limited — Business Card</title>
<link rel="stylesheet" href="https://fonts.googleapis.com/css2?family=Montserrat:wght@700&family=Poppins:wght@400;500&display=swap">
<style>
  :root {
    --backdrop: #2b2b2d;
    --card-black: #050505;
    --card-white: #ffffff;
    --gold: #f7b324;
    --silver: #b9b9b9;
    --ink: #2e2e2e;
    --ink-soft: #3a3a3a;
  }
  * { margin: 0; padding: 0; box-sizing: border-box; }
  html, body { width: 1200px; height: 900px; overflow: hidden; }
  body {
    background: var(--backdrop);
    font-family: "Poppins", sans-serif;
    position: relative;
  }
  .card {
    position: absolute;
    left: 280px;
    width: 640px;
    height: 366px;
    border-radius: 22px;
    overflow: hidden;
  }
  .card--back { top: 70px; background: var(--card-black); }
  .card--front { top: 464px; background: var(--card-white); }

  /* Back side */
  .back-brand {
    position: absolute;
    inset: 0;
    display: flex;
    align-items: center;
    justify-content: center;
    gap: 22px;
  }
  .brand-dot {
    width: 74px; height: 74px;
    border-radius: 50%;
    border: 9px solid var(--gold);
  }
  .brand-name {
    font-family: "Montserrat", sans-serif;
    font-weight: 700;
    letter-spacing: 0.08em;
    text-transform: uppercase;
    line-height: 1.1;
  }
  .back-brand .brand-name { color: var(--gold); font-size: 34px; }

  /* Front side */
  .front-ring {
    position: absolute;
    left: 380px;
    top: 30px;
    width: 380px; height: 380px;
    border-radius: 50%;
    border: 44px solid var(--gold);
  }
  .front-info {
    position: absolute;
    left: 44px;
    top: 40px;
    max-width: 330px;
  }
  .front-info .brand-name {
    color: var(--ink);
    font-size: 26px;
    letter-spacing: 0.06em;
  }
  .person { margin-top: 26px; }
  .person-name {
    font-family: "Montserrat", sans-serif;
    font-weight: 700;
    font-size: 22px;
    letter-spacing: 0.06em;
    color: var(--ink);
  }
  .person-role {
    font-family: "Montserrat", sans-serif;
    font-weight: 700;
    font-size: 12px;
    letter-spacing: 0.12em;
    color: var(--gold);
    margin-top: 2px;
  }
  .contact { list-style: none; margin-top: 20px; }
  .contact li {
    display: flex;
    align-items: flex-start;
    gap: 12px;
    font-size: 13.5px;
    color: var(--ink-soft);
    line-height: 1.45;
    margin-bottom: 4px;
  }
  .contact li.address { margin-top: 8px; }
  .contact svg { width: 14px; height: 14px; flex: none; margin-top: 3px; }
</style>
</head>
<body>

  <section class="card card--back" aria-label="Card back">
    <div class="back-brand">
      <span class="brand-dot"></span>
      <div class="brand-name">Morvik<br>Company Limited</div>
    </div>
  </section>

  <section class="card card--front" aria-label="Card front">
    <span class="front-ring"></span>
    <div class="front-info">
      <div class="brand-name">Morvik<br>Company Limited</div>
      <div class="person">
        <div class="person-name">DANIEL REYES</div>
        <div class="person-role">MANAGING DIRECTOR</div>
      </div>
      <ul class="contact">
        <li>
          <svg viewBox="0 0 24 24"><path fill="#7cc242" d="M6.6 10.8a15.1 15.1 0 0 0 6.6 6.6l2.2-2.2a1 1 0 0 1 1-.25 11.4 11.4 0 0 0 3.6.57 1 1 0 0 1 1 1V20a1 1 0 0 1-1 1A17 17 0 0 1 3 4a1 1 0 0 1 1-1h3.5a1 1 0 0 1 1 1c0 1.25.2 2.45.57 3.57a1 1 0 0 1-.25 1z"/></svg>
          555 210 3870
        </li>
        <li>
          <svg viewBox="0 0 24 24"><rect x="2" y="5" width="20" height="14" rx="1" fill="var(--gold)"/><path d="M2 6l10 7 10-7" fill="none" stroke="#fff" stroke-width="1.6"/></svg>
          info@morvikcompanylimited.com
        </li>
        <li>
          <svg viewBox="0 0 24 24" fill="none" stroke="var(--gold)" stroke-width="1.8"><circle cx="12" cy="12" r="9"/><path d="M3 12h18M12 3c3 3.2 3 14.8 0 18M12 3c-3 3.2-3 14.8 0 18"/></svg>
          www.morvikcompanylimited.com
        </li>
        <li class="address">
          <svg viewBox="0 0 24 24"><path fill="var(--gold)" d="M12 2a7 7 0 0 0-7 7c0 5.2 7 13 7 13s7-7.8 7-13a7 7 0 0 0-7-7zm0 9.5A2.5 2.5 0 1 1 12 6.5a2.5 2.5 0 0 1 0 5z"/></svg>
          <span>118 Linden Street NW<br>Suite 210, Brookhaven<br>MI 49620</span>
        </li>
      </ul>
    </div>
  </section>

</body>
</html>
```